VELINTA Promotions - Business Card Design Project

We are looking for a classy business cards for Promotion Company based in Toronto, Canada named Velinta Promotions.

Velinta Promotions has an idea and vision to set high standard, be EXCLUSIVE and attract a group of people that will follow us through events we promote (night clubs, brand promotions, music events, and sport events)

We want to present a high standards and classy image to the others...
Updates

Target Market(s)

male/female age 25-40 Target: business owners young entrepreneur - clubing industry - media industry - promotion industry - marketing media industry

Industry/Entity Type

Events

Requirements
Must have
• business cards should be classy, make people feel exclusive , make people react ..

```html
<!DOCTYPE html>
<html lang="en">
<head>
<meta charset="utf-8">
<title>Velinta Promotions – Business Card</title>
<link rel="stylesheet" href="https://fonts.googleapis.com/css2?family=Open+Sans:wght@300;400;700&family=PT+Sans+Narrow&display=swap">
<style>
  :root {
    --brand-cyan: #45f6ff;
    --paper: #ffffff;
    --ink-light: #ffffff;
  }
  html, body {
    margin: 0;
    padding: 0;
    overflow: hidden;
    background: var(--paper);
  }
  .card {
    position: relative;
    width: 1200px;
    height: 751px;
    background: var(--paper);
    overflow: hidden;
  }
  .brand-name {
    position: absolute;
    left: 0;
    right: 0;
    top: 88px;
    margin: 0;
    text-align: center;
    font-family: "Open Sans", sans-serif;
    font-weight: 400;
    font-size: 92px;
    line-height: 1;
    letter-spacing: 2px;
    color: var(--brand-cyan);
  }
  .info-band {
    position: absolute;
    left: 0;
    top: 251px;
    width: 1200px;
    height: 500px;
    background: var(--brand-cyan);
  }
  .person {
    position: absolute;
    right: 65px;
    font-family: "Open Sans", sans-serif;
    color: var(--ink-light);
    text-align: right;
    line-height: 1;
    margin: 0;
  }
  .person-name {
    top: 317px;
    font-size: 46px;
    font-weight: 700;
  }
  .person-title {
    top: 383px;
    font-size: 46px;
    font-weight: 300;
  }
  .contact {
    position: absolute;
    margin: 0;
    padding: 0;
    list-style: none;
    font-family: "PT Sans Narrow", sans-serif;
    font-size: 44px;
    line-height: 67px;
    color: var(--ink-light);
  }
  .contact-office {
    left: 76px;
    top: 432px;
  }
  .contact-direct {
    right: 65px;
    top: 566px;
    text-align: right;
  }
</style>
</head>
<body>
  <main class="card">
    <h1 class="brand-name">VELINTA Promotions</h1>

    <section class="info-band">
    </section>

    <p class="person person-name">Dana MERCER</p>
    <p class="person person-title">Director</p>

    <ul class="contact contact-office">
      <li>12 St. ............................</li>
      <li>Toronto - CANADA</li>
      <li>T. 416550182 • F. 41655073 •</li>
      <li>w. www.velinta.com</li>
    </ul>

    <ul class="contact contact-direct">
      <li>d.mercer@velinta.com</li>
      <li>054781209</li>
    </ul>
  </main>
</body>
</html>
```